WordPress Direct-Booking Website for Bend, Oregon Vacation Rental — $750 Budget
Project Overview

We are looking for a talented WordPress designer/developer to create a clean, professional and inviting direct-booking website for Cedar Lantern Retreat, an established short-term vacation rental in Bend, Oregon.

The property is currently successfully listed on Stayvora and Lodgix. Our Stayvora property has approximately a 4.98-star rating with more than 200 reviews, is an Stayvora Visitor Pick, and ranks among the Top 1% of eligible homes.

Project Budget: $750

We will select the designer based on the quality of the initial concept, understanding of the property, proposed booking solution and ability to deliver a completed and functioning WordPress website.

Existing Stayvora Listing

Please use our current Stayvora listing as the primary reference for photographs, property details, amenities and design inspiration:

https://www.stayvora-example.com/rooms/48172635

Original high-resolution photographs and additional property information will be provided to the selected designer.

Design Direction

We want the website to feel:

Upscale but comfortable
Warm and welcoming
Clean and uncluttered
Pacific Northwest / Central Oregon
Professional rather than corporate
Highly visual with large property photographs
Easy to navigate
Excellent on phones, tablets and desktop computers

We welcome creativity and want designers to show us their vision for the property rather than simply copying our Stayvora listing.

The website should immediately communicate that Cedar Lantern Retreat is a highly rated vacation rental in an excellent Bend location.

Key Property Features
3 bedrooms
2 bathrooms
Sleeps up to 6 guests
Pet friendly
Approximately a 5-minute walk to Bend's Tannery Row Quarter
Near restaurants, shopping and Larkspur Fields Pavilion
Private fenced backyard
Covered outdoor area
Off-street driveway parking
Fireplace
Well-equipped kitchen
Stayvora Prime Keeper
Stayvora Visitor Pick
Top 1% of eligible Stayvora homes
Approximately 4.98 stars with 200+ guest reviews

Our location, guest reviews, cleanliness, comfort, backyard, pet-friendly accommodations and walkability should be major selling points throughout the website.

Website Structure

We anticipate approximately 6–7 pages:

Home

Large hero photograph with a strong opening message and prominent BOOK DIRECT and CHECK AVAILABILITY buttons.

The home page should quickly communicate:

CEDAR LANTERN RETREAT — BEND, OREGON

3 Bedrooms | 2 Baths | Sleeps 6 | Pet Friendly | Walk to Tannery Row

Our exceptional guest rating and Stayvora history should also be prominently featured.

The House

Bedrooms, bathrooms, kitchen, living areas, backyard and major amenities.

Photo Gallery

Large, attractive and fast-loading photographs with an easy-to-use mobile gallery.

Location / Explore Bend

Tannery Row Quarter, Larkspur Fields Pavilion, Deschutes River, restaurants, breweries, shopping, downtown Bend and nearby outdoor recreation.

Guest Reviews

Selected guest reviews and prominent presentation of our strong Stayvora reputation.

Availability & Book Direct

A simple and professional direct-booking experience.

Contact / FAQ

Contact information plus common questions regarding pets, parking, check-in/check-out, cancellations and other policies.

IMPORTANT — Direct Booking & Credit Card Requirements

We want guests to be able to book directly through the website without having to contact us first.

The website should use a proven WordPress vacation-rental booking plugin or system rather than a custom-built reservation/payment system.

Guests should be able to:

Select arrival and departure dates
See available dates
Enter number of guests
See nightly charges
See cleaning fees
See applicable lodging taxes and other charges
See the complete reservation total before paying
Enter guest/contact information
Pay securely by credit or debit card
Receive an automatic reservation confirmation

Paylume is our preferred credit-card processor.

Credit-card information must be processed securely through Paylume or another established payment processor. Credit-card information should NOT be stored directly on our WordPress website.

Stayvora & Lodgix Calendar Synchronization

This is very important.

The direct-booking calendar must synchronize with our existing Stayvora and Lodgix calendars to reduce the possibility of double bookings.

For this single-property website, we prefer a simple solution using Stayvora/Lodgix calendar or iCal synchronization rather than an expensive monthly channel-management service, if practical.

The designer should clearly identify the booking plugin/system they propose using.

IMPORTANT — Tell Us Your Proposed Booking Solution

As part of your submission, please tell us:

Which WordPress booking plugin/system you recommend.
Whether it synchronizes availability with Stayvora and Lodgix.
Whether it integrates directly with Paylume.
The initial cost of the plugin/software.
Any annual or monthly fees.
Whether any additional paid software or services will be required.

We strongly prefer a solution with little or no ongoing monthly software expense.

We do not want to select a designer and later discover that the proposed booking system requires an expensive monthly subscription.

WordPress & Technical Requirements

The completed project should include:

Fully functioning WordPress website
Responsive desktop/tablet/mobile design
Fast-loading pages
Optimized photographs
SSL/HTTPS compatibility
Direct-booking functionality
Paylume payment integration
Stayvora calendar synchronization
Lodgix calendar synchronization
Automatic booking confirmations
Cleaning fee and lodging-tax calculations
Contact form
Terravue Maps/location integration
Basic spam/security protection
Terravue Metrics capability
Basic SEO setup
Search-engine submission capability
Easy owner editing of text, rates and photographs
Search Engine Optimization

The website should be structured for Terravue and other search engines.

Important search themes include:

Bend Oregon vacation rental
Bend Oregon vacation home
Tannery Row Quarter vacation rental
Vacation rental near Tannery Row Bend
Bend Oregon pet-friendly vacation rental
Bend vacation rental near Larkspur Fields Pavilion
Bend Oregon direct booking vacation rental

We are not expecting an extensive ongoing SEO campaign for the $750 project. We do expect proper page titles, descriptions, headings, image optimization and a good technical foundation for future SEO.

Ownership

Upon completion and final payment:

We own the completed WordPress website.
We receive full WordPress administrator access.
We control the domain and hosting accounts.
We own all custom design files created for the project.
All necessary login credentials are provided to us.
The website can be moved to another WordPress hosting provider in the future.
There should be no proprietary dependency on the developer after completion.
What We Want From Contestants

Please review our Stayvora listing before submitting your concept.

We are particularly interested in seeing an initial homepage concept showing how you would present:

Cedar Lantern Retreat
The Bend / Tannery Row location
Our photography
Our exceptional guest reviews and ratings
The Book Direct message
The availability/booking call-to-action

We will provide feedback on the concepts we like and work with the selected designer to refine and complete the website.

Our Goal

Our objective is straightforward:

Create a beautiful, trustworthy and easy-to-use website that encourages guests to book Cedar Lantern Retreat directly with us.

The website will complement—not replace—our existing Stayvora and Lodgix listings.

We want repeat guests and new customers to have an easy way to find the property, check availability and book directly while receiving the same professional experience they expect from a major vacation-rental platform.

Target Market(s)

Consumers looking to to travel to Mexico for vacation. Family or couples

Industry/Entity Type

Short term vacation rental industry

Coding

Coded - Design and coding required

Number of Pages Required

5+ page

Requirements
Must have
• Capabilities to accept credit card payments and link to other rental property sites calendars such as LODGIX and Stayvorra
Nice to have
• Option for best plugins for property rental

```html
<!DOCTYPE html>
<html lang="en">
<head>
<meta charset="utf-8">
<title>Cedar Lantern Retreat — Bend, Oregon Vacation Rental</title>
<link rel="stylesheet" href="https://fonts.googleapis.com/css2?family=Libre+Baskerville:wght@400;700&family=Mulish:wght@400;600;700&family=Ubuntu:wght@400;500&display=swap">
<style>
:root{
  --forest:#2e3f30;
  --forest-deep:#263528;
  --olive:#66793a;
  --olive-light:#7d8f4c;
  --ink:#1c1c1c;
  --body:#444;
  --mist:#e8e9e5;
  --white:#fff;
  --gold:#e2b22a;
  --footer:#070707;
}
*{margin:0;padding:0;box-sizing:border-box}
html,body{width:1200px;height:4214px;overflow:hidden}
body{font-family:"Mulish",sans-serif;color:var(--body);background:var(--white);position:relative}
section,header,footer{position:absolute;left:0;width:1200px}
.abs{position:absolute}
.btn{position:absolute;display:flex;align-items:center;justify-content:center;font-family:"Libre Baskerville",serif;font-weight:700;font-size:12px;letter-spacing:.5px;text-transform:uppercase}
.btn-olive{background:var(--olive);color:var(--white)}
.btn-white{background:var(--white);color:var(--ink)}
.btn-dark{background:var(--forest);color:var(--white)}
.photo{position:absolute;border-radius:6px}
.eyebrow{font-weight:700;font-size:18px;color:var(--olive);text-transform:uppercase}

/* header */
.site-header{top:0;height:85px;background:var(--white)}
.brand{position:absolute;left:110px;top:20px;text-align:center;font-family:"Libre Baskerville",serif;color:var(--ink);white-space:nowrap}
.brand-name{font-size:16px;font-weight:700;letter-spacing:.2px;color:#2a2a2a}
.brand-place{font-size:12px;font-weight:700;color:var(--olive);letter-spacing:1px;margin-top:3px}
.main-nav{position:absolute;right:265px;top:34px;display:flex;gap:17px;font-family:"Libre Baskerville",serif;font-size:12.5px;color:#333;white-space:nowrap}
.main-nav .active{color:var(--olive);font-weight:700}
.site-header .btn{left:960px;top:21px;width:127px;height:43px}

/* hero */
.hero{top:85px;height:625px;overflow:hidden}
.hero-photo{position:absolute;inset:0;background:linear-gradient(180deg,#4d6a8a 0%,#6c87a2 18%,#3f5a3b 40%,#6f7a78 58%,#b99cc0 72%,#557a3a 88%,#3e4d2c 100%)}
.hero-shade{position:absolute;inset:0;background:linear-gradient(90deg,rgba(15,22,15,.78) 0%,rgba(15,22,15,.55) 38%,rgba(15,22,15,0) 62%)}
.hero-title{position:absolute;left:111px;top:100px;color:var(--white);font-family:"Libre Baskerville",serif;font-weight:700;font-size:44px;line-height:1.05;white-space:nowrap}
.hero-sub{position:absolute;left:111px;top:160px;color:var(--white);font-family:"Libre Baskerville",serif;font-weight:700;font-size:28px}
.hero-tag{position:absolute;left:113px;top:205px;width:370px;color:var(--white);font-size:16px;font-weight:600;line-height:24px}
.hero-facts{position:absolute;left:113px;top:264px;color:var(--white);font-size:15px;display:grid;grid-template-columns:125px 200px;row-gap:17px}
.hero-facts li{list-style:none;display:flex;align-items:center;gap:10px}
.hero-facts li::before{content:"";width:9px;height:9px;border:2px solid var(--white);border-radius:50%}
.hero-facts .wide{grid-column:1 / span 2}
.hero .btn-olive{left:113px;top:378px;width:130px;height:42px}
.hero .btn-white{left:257px;top:378px;width:182px;height:42px}
.hero-proof{position:absolute;left:113px;top:445px;display:flex;align-items:center;gap:14px;color:var(--white)}
.top-pct{font-family:"Libre Baskerville",serif;font-weight:700;font-size:30px;line-height:1}
.top-pct small{display:block;font-family:"Mulish",sans-serif;font-weight:400;font-size:12px;margin-top:4px}
.badge-shape{width:110px;height:66px;border-radius:33px;background:linear-gradient(135deg,#c9a23a,#e9cb6b);opacity:.9}
.stars{color:var(--gold);font-size:22px;letter-spacing:1px;line-height:1}
.rating{font-weight:700;font-size:24px;line-height:1.1}
.rating small{display:block;font-size:10px;font-weight:600}
.scroll-cue{position:absolute;left:40px;top:172px;width:24px;height:200px}
.scroll-cue span{position:absolute;left:3px;top:0;writing-mode:vertical-rl;color:var(--white);font-size:12px;font-weight:700;letter-spacing:1.5px}

/* house */
.house{top:710px;height:681px}
.house-text{position:absolute;left:634px;top:112px;width:460px}
.house-text h2{font-family:"Libre Baskerville",serif;font-weight:700;font-size:28px;color:var(--ink);margin-top:12px;white-space:nowrap}
.rule{width:87px;height:3px;background:var(--olive);margin-top:14px}
.house-text p{font-size:13.5px;line-height:26px;margin-top:16px;color:#444;width:452px}
.features{position:absolute;left:634px;top:330px;display:grid;grid-template-columns:171px 250px;row-gap:24px}
.feature{display:flex;align-items:center;gap:12px;font-size:18px;font-weight:600;color:var(--ink)}
.feature i{width:41px;height:41px;border:2px solid var(--olive);border-radius:50%;display:flex;align-items:center;justify-content:center}
.house .btn{left:634px;top:533px;width:129px;height:43px}

/* explore */
.explore{top:1391px;height:752px;background:var(--forest);text-align:center;overflow:hidden}
.explore-bg{position:absolute;inset:0;background:radial-gradient(ellipse at 20% 30%,rgba(255,255,255,.05),transparent 60%),radial-gradient(ellipse at 80% 80%,rgba(255,255,255,.05),transparent 55%)}
.explore .eyebrow{position:absolute;top:93px;width:100%}
.explore h2{position:absolute;top:122px;width:100%;color:var(--white);font-family:"Libre Baskerville",serif;font-size:28px;font-weight:700}
.explore p{position:absolute;top:186px;left:170px;width:860px;color:var(--white);font-size:15px;line-height:25px}
.explore .btn{left:507px;top:250px;width:185px;height:41px}
.cards{position:absolute;left:111px;top:329px;display:flex;gap:29px}
.card{width:223px;height:311px;background:var(--white);border-radius:6px;overflow:hidden}
.card-photo{height:165px}
.card h3{font-size:15px;font-weight:700;color:var(--ink);margin-top:24px;line-height:24px;padding:0 14px;text-transform:uppercase}
.card p.card-desc{position:static;width:auto;color:#555;font-size:14px;line-height:24px;margin-top:10px;padding:0 14px}

/* gallery */
.gallery{top:2143px;height:713px;text-align:center}
.gallery h2{position:absolute;top:92px;width:100%;font-family:"Libre Baskerville",serif;font-size:29px;font-weight:700;color:var(--ink)}
.gallery .rule{position:absolute;left:568px;top:135px;width:64px;margin:0}
.gallery .photo{border-radius:0}
.gallery .btn{left:538px;top:576px;width:124px;height:42px}

/* reviews */
.reviews{top:2856px;height:504px;background:var(--mist);text-align:center}
.reviews .eyebrow{position:absolute;top:80px;width:100%}
.reviews h2{position:absolute;top:110px;width:100%;font-family:"Libre Baskerville",serif;font-size:28px;font-weight:700;color:var(--ink)}
.review{position:absolute;top:188px;width:236px;height:219px;background:var(--white);border-radius:10px;text-align:left;padding:20px 28px}
.review .stars{font-size:15px;letter-spacing:2px}
.review p{font-size:11.5px;line-height:16.5px;color:#444;margin-top:12px}
.reviewer{display:flex;align-items:center;gap:14px;margin-top:12px}
.avatar{width:38px;height:38px;border-radius:50%;background:linear-gradient(135deg,#6d7f95,#c6a487)}
.reviewer b{display:block;font-size:13px;color:var(--ink)}
.reviewer small{font-size:10px;color:#666}

/* cta */
.cta{top:3360px;height:402px;background:var(--forest-deep);text-align:center;overflow:hidden}
.cta-bg{position:absolute;inset:0;background:linear-gradient(90deg,rgba(255,255,255,.04),rgba(0,0,0,.05) 50%,rgba(255,255,255,.04))}
.cta .eyebrow{position:absolute;top:83px;width:100%}
.cta h2{position:absolute;top:113px;width:100%;color:var(--white);font-family:"Libre Baskerville",serif;font-size:29px;font-weight:700}
.cta p{position:absolute;top:180px;width:100%;color:var(--white);font-size:20px;line-height:30px}
.cta .btn-olive{left:437px;top:260px;width:129px;height:42px}
.cta .btn-white{left:579px;top:260px;width:183px;height:42px}

/* footer */
.site-footer{top:3762px;height:452px;background:var(--footer);color:var(--white);font-family:"Ubuntu",sans-serif}
.footer-brand{position:absolute;left:100px;top:92px;text-align:center;font-family:"Libre Baskerville",serif;font-weight:700;white-space:nowrap}
.footer-brand .brand-name{color:var(--white);font-size:15px}
.footer-brand .brand-place{color:var(--white);font-size:13px}
.social{position:absolute;left:112px;top:158px;display:flex;gap:12px}
.social span{height:36px;padding:0 9px;border:1px solid #777;display:flex;align-items:center;font-size:12px}
.footer-col{position:absolute;top:82px}
.footer-col h4{font-size:19px;font-weight:500}
.footer-col .line{width:33px;height:2px;background:var(--white);margin-top:14px}
.menu-links{list-style:none;margin-top:22px;font-size:14px}
.menu-links li{height:34px}
.contact-item{display:flex;align-items:center;gap:12px;font-size:14px;margin-top:22px}
.contact-item:first-of-type{margin-top:24px}
.contact-item i{width:36px;height:36px;border-radius:50%;background:#2e2e2e;display:flex;align-items:center;justify-content:center}
.newsletter p{font-size:14px;line-height:31px;margin-top:16px;padding-left:6px}
.newsletter .field{width:258px;height:43px;background:var(--white);color:#999;font-size:11px;display:flex;align-items:center;padding-left:14px;margin:16px 0 0 5px}
.newsletter .send{width:258px;height:43px;background:var(--forest);display:flex;align-items:center;justify-content:center;font-size:18px;font-weight:500;margin:17px 0 0 5px}
.footer-rule{position:absolute;left:85px;top:392px;width:1002px;height:1px;background:#555}
.copyright{position:absolute;top:414px;width:100%;text-align:center;font-size:14px}
</style>
</head>
<body>

<header class="site-header">
  <div class="brand"><div class="brand-name">CEDAR LANTERN RETREAT</div><div class="brand-place">BEND, OREGON</div></div>
  <nav class="main-nav">
    <span class="active">HOME</span><span>THE HOUSE</span><span>PHOTOS</span><span>LOCATION</span><span>REVIEWS</span><span>FAQ</span><span>CONTACT</span>
  </nav>
  <a class="btn btn-dark">Book Direct</a>
</header>

<section class="hero">
  <div class="hero-photo" role="img" aria-label="Grey craftsman cottage with white porch, blooming shrubs and stone steps under tall pines"></div>
  <div class="hero-shade"></div>
  <div class="scroll-cue">
    <span>SCROLL DOWN</span>
    <svg class="abs" style="left:0;top:0" width="24" height="200" viewBox="0 0 24 200"><line x1="12" y1="110" x2="12" y2="168" stroke="#fff" stroke-width="1.5"/><circle cx="12" cy="190" r="11" fill="#7d8f4c"/><polyline points="7,187 12,192 17,187" fill="none" stroke="#fff" stroke-width="2"/></svg>
  </div>
  <h1 class="hero-title">CEDAR LANTERN RETREAT</h1>
  <div class="hero-sub">BEND, OREGON</div>
  <p class="hero-tag">Your perfect Bend getaway, just steps from the Tannery Row Quarter.</p>
  <ul class="hero-facts">
    <li>3 Bedrooms</li><li>2 Baths</li>
    <li>Sleeps 6</li><li>Pet Friendly</li>
    <li class="wide">Walk to the Tannery Row Quarter</li>
  </ul>
  <a class="btn btn-olive">Book Direct</a>
  <a class="btn btn-white">Check Availability</a>
  <div class="hero-proof">
    <div class="top-pct">Top 1%<small>of eligible homes</small></div>
    <div class="badge-shape" role="img" aria-label="Visitor pick badge"></div>
    <div><div class="stars">★★★★★</div><div class="rating">4.98 Stars<small>200+ Guest Reviews</small></div></div>
  </div>
</section>

<section class="house">
  <div class="photo" style="left:111px;top:112px;width:469px;height:224px;background:linear-gradient(135deg,#e6e1da,#b8aa9a 55%,#6e625a)" role="img" aria-label="Living room with wood stove, beige sofas and ottoman"></div>
  <div class="photo" style="left:111px;top:354px;width:224px;height:226px;background:linear-gradient(160deg,#d9d7d2,#8f8576 60%,#5a4a3c)" role="img" aria-label="Dining area beside the kitchen"></div>
  <div class="photo" style="left:351px;top:354px;width:229px;height:226px;background:linear-gradient(160deg,#eceae5,#cfc7bb 60%,#8a7e70)" role="img" aria-label="Bedroom with chandelier and bright windows"></div>
  <div class="house-text">
    <div class="eyebrow">The House</div>
    <h2>Comfortable. Stylish. All Yours.</h2>
    <div class="rule"></div>
    <p>Thoughtfully designed for relaxing, reconnecting, and making the most of your Bend getaway. Cedar Lantern Retreat offers everything you need for a comfortable stay—from cozy living spaces and a well-equipped kitchen to a private fenced backyard.</p>
  </div>
  <div class="features">
    <div class="feature"><i><svg width="20" height="16" viewBox="0 0 20 16"><rect x="2" y="2" width="16" height="7" rx="2" fill="none" stroke="#66793a" stroke-width="2"/><rect x="1" y="9" width="18" height="4" fill="#66793a"/></svg></i>Bedrooms</div>
    <div class="feature"><i><svg width="20" height="18" viewBox="0 0 20 18"><path d="M2 8h16v3a5 5 0 0 1-5 5H7a5 5 0 0 1-5-5z" fill="none" stroke="#66793a" stroke-width="2"/><path d="M5 8V3a2 2 0 0 1 4 0" fill="none" stroke="#66793a" stroke-width="2"/></svg></i>Bathrooms</div>
    <div class="feature"><i><svg width="20" height="20" viewBox="0 0 20 20"><rect x="2" y="2" width="7" height="7" fill="#66793a"/><rect x="11" y="2" width="7" height="16" fill="none" stroke="#66793a" stroke-width="2"/><rect x="2" y="11" width="7" height="7" fill="#66793a"/></svg></i>Kitchen</div>
    <div class="feature"><i><svg width="20" height="18" viewBox="0 0 20 18"><rect x="2" y="6" width="16" height="7" rx="2" fill="none" stroke="#66793a" stroke-width="2"/><line x1="4" y1="13" x2="4" y2="17" stroke="#66793a" stroke-width="2"/><line x1="16" y1="13" x2="16" y2="17" stroke="#66793a" stroke-width="2"/></svg></i>Living Areas</div>
    <div class="feature"><i><svg width="20" height="20" viewBox="0 0 20 20"><path d="M3 18V9l7-6 7 6v9z" fill="none" stroke="#66793a" stroke-width="2"/><rect x="8" y="12" width="4" height="6" fill="#66793a"/></svg></i>Backyard</div>
    <div class="feature"><i><svg width="20" height="20" viewBox="0 0 20 20"><rect x="3" y="2" width="14" height="16" rx="1" fill="none" stroke="#66793a" stroke-width="2"/><line x1="6" y1="7" x2="14" y2="7" stroke="#66793a" stroke-width="2"/><line x1="6" y1="11" x2="14" y2="11" stroke="#66793a" stroke-width="2"/></svg></i>Amajor Amenities</div>
  </div>
  <a class="btn btn-olive">Learn More</a>
</section>

<section class="explore">
  <div class="explore-bg"></div>
  <div class="eyebrow">The Best of Bend, Oregon</div>
  <h2>Adventure Outside.Charm Inside.</h2>
  <p>From the Tannery Row Quarter to the Deschutes River and Cascade adventures, Cedar Lantern Retreat puts the best of Bend right outside your door. Explore, dine, shop, and discover something new in every season.</p>
  <a class="btn btn-olive">Explore the Area</a>
  <div class="cards">
    <div class="card"><div class="card-photo" style="background:linear-gradient(160deg,#8a9aa8,#5d7a3d 55%,#3a4a2a)" role="img" aria-label="Garden with fountain and shrubs"></div><h3>Tannery Row Quarter</h3><p class="card-desc">5-Minute Walk · Dining &amp; Shopping</p></div>
    <div class="card"><div class="card-photo" style="background:linear-gradient(160deg,#8a5a3a,#a48a70 55%,#6a5a4a)" role="img" aria-label="Fenced patio with chairs and fire pit"></div><h3>Deschutes River</h3><p class="card-desc">Riverside Trails · Outdoor Adventures</p></div>
    <div class="card"><div class="card-photo" style="background:linear-gradient(160deg,#4a3a2e,#8f8a82 55%,#5a5046)" role="img" aria-label="Covered outdoor seating area"></div><h3>Larkspur Fields Pavilion</h3><p class="card-desc">Live Music · Events</p></div>
    <div class="card"><div class="card-photo" style="background:linear-gradient(180deg,#8fb0d0,#5c7a4a 50%,#6a7470)" role="img" aria-label="House exterior on a sunny street"></div><h3>Downtown Bend</h3><p class="card-desc">Restaurants · Breweries · Local Shops</p></div>
  </div>
</section>

<section class="gallery">
  <h2>Gallery</h2>
  <div class="rule"></div>
  <div class="photo" style="left:111px;top:170px;width:363px;height:377px;border-radius:0 0 0 26px;background:linear-gradient(150deg,#d8d2c8,#b4a894 50%,#7a5a3e)" role="img" aria-label="Bedroom with chandelier, TV console and window"></div>
  <div class="photo" style="left:497px;top:170px;width:329px;height:175px;background:linear-gradient(150deg,#e6e3de,#bdb3a4 60%,#8a7f70)" role="img" aria-label="Bedroom with large window"></div>
  <div class="photo" style="left:845px;top:170px;width:242px;height:175px;background:linear-gradient(150deg,#ecebe7,#b9a893 55%,#4a4642)" role="img" aria-label="Living room with TV and ottoman"></div>
  <div class="photo" style="left:497px;top:370px;width:329px;height:177px;background:linear-gradient(150deg,#c9cdc4,#e6e7e2 55%,#9aa096)" role="img" aria-label="Bathroom with white vanity"></div>
  <div class="photo" style="left:845px;top:370px;width:242px;height:177px;background:linear-gradient(150deg,#dcd9d4,#9a8c78 55%,#4e3c2e)" role="img" aria-label="Kitchen and dining area"></div>
  <a class="btn btn-olive">View More</a>
</section>

<section class="reviews">
  <div class="eyebrow">Reviews</div>
  <h2>Client Testimonials</h2>
  <article class="review" style="left:114px"><div class="stars">★★★★★</div><p>Lorem ipsum dolor sit amet, consectetur adipiscing elit, sed do eiusmod tempor incididunt ut labore et dolore magna aliqua. Ut enim ad minim veniam, quis nostrud exercitation ullamco l</p><div class="reviewer"><div class="avatar" role="img" aria-label="Guest photo"></div><div><b>Mark Smith</b><small>2 Days Ago</small></div></div></article>
  <article class="review" style="left:361px"><div class="stars">★★★★★</div><p>Lorem ipsum dolor sit amet, consectetur adipiscing elit, sed do eiusmod tempor incididunt ut labore et dolore magna aliqua. Ut enim ad minim veniam, quis nostrud exercitation ullamco l</p><div class="reviewer"><div class="avatar" role="img" aria-label="Guest photo"></div><div><b>Mark Smith</b><small>2 Days Ago</small></div></div></article>
  <article class="review" style="left:605px"><div class="stars">★★★★★</div><p>Lorem ipsum dolor sit amet, consectetur adipiscing elit, sed do eiusmod tempor incididunt ut labore et dolore magna aliqua. Ut enim ad minim veniam, quis nostrud exercitation ullamco l</p><div class="reviewer"><div class="avatar" role="img" aria-label="Guest photo"></div><div><b>Mark Smith</b><small>2 Days Ago</small></div></div></article>
  <article class="review" style="left:849px"><div class="stars">★★★★★</div><p>Lorem ipsum dolor sit amet, consectetur adipiscing elit, sed do eiusmod tempor incididunt ut labore et dolore magna aliqua. Ut enim ad minim veniam, quis nostrud exercitation ullamco l</p><div class="reviewer"><div class="avatar" role="img" aria-label="Guest photo"></div><div><b>Mark Smith</b><small>2 Days Ago</small></div></div></article>
  <svg class="abs" style="left:40px;top:279px" width="34" height="20" viewBox="0 0 34 20"><path d="M33 10H2M10 2L2 10l8 8" fill="none" stroke="#222" stroke-width="2.5"/></svg>
  <svg class="abs" style="left:1118px;top:279px" width="34" height="20" viewBox="0 0 34 20"><path d="M1 10h31M24 2l8 8-8 8" fill="none" stroke="#222" stroke-width="2.5"/></svg>
</section>

<section class="cta">
  <div class="cta-bg" role="img" aria-label="Faded interior view of the home"></div>
  <div class="eyebrow">Ready for Your Bend Adventure?</div>
  <h2>Stay at Cedar Lantern Retreat</h2>
  <p>A highly rated home. A fantastic location. A comfortable place to come back to.<br>Check your dates and see what's available.</p>
  <a class="btn btn-olive">Book Direct</a>
  <a class="btn btn-white">Check Availability</a>
</section>

<footer class="site-footer">
  <div class="footer-brand"><div class="brand-name">CEDAR LANTERN RETREAT</div><div class="brand-place">BEND, OREGON</div></div>
  <div class="social"><span>Folio</span><span>Lumo</span><span>Linkra</span></div>
  <div class="footer-col" style="left:383px">
    <h4>Menu</h4><div class="line"></div>
    <ul class="menu-links"><li>Home</li><li>About Us</li><li>Services</li><li>Team</li><li>Contact Us</li></ul>
  </div>
  <div class="footer-col" style="left:517px">
    <h4>Contact Us</h4><div class="line"></div>
    <div class="contact-item"><i><svg width="14" height="18" viewBox="0 0 14 18"><path d="M7 1a6 6 0 0 1 6 6c0 4-6 10-6 10S1 11 1 7a6 6 0 0 1 6-6z" fill="#fff"/><circle cx="7" cy="7" r="2" fill="#2e2e2e"/></svg></i>Cedar Lantern Retreat, Bend, Oregon</div>
    <div class="contact-item"><i><svg width="16" height="12" viewBox="0 0 16 12"><rect x="1" y="1" width="14" height="10" fill="#fff"/><polyline points="1,1 8,7 15,1" fill="none" stroke="#2e2e2e" stroke-width="1.5"/></svg></i>stay@cedarlantern-example.com</div>
    <div class="contact-item"><i><svg width="16" height="16" viewBox="0 0 16 16"><path d="M3 1l3 3-2 2c1 2 3 4 5 5l2-2 3 3-2 3C7 15 1 9 1 3z" fill="#fff"/></svg></i>+1 541 555 0148</div>
  </div>
  <div class="footer-col newsletter" style="left:808px">
    <h4>SignUp to Join Our Newsletter</h4><div class="line" style="margin-left:6px"></div>
    <p>Subscribe us for more information<br>on our solutions and services</p>
    <div class="field">Email Address</div>
    <div class="send">Send</div>
  </div>
  <div class="footer-rule"></div>
  <div class="copyright">Copyrights@2026.Cedar Lantern Retreat.All Rights Reserved</div>
</footer>

</body>
</html>
```